International Bike and Bike Clothing distribution business needs business card design. Business is

We need a business card design for our Bike Brand distribution business. Want the company name on one side and rep/gm contact details on other side. Contact details would include, name, title, email, phone, postal address. Needs to be a bit edgy, dealing with a sporting/cycling community so can be casual but professional. Company name is 'Brisko Bike Brands' and would like to see 'Brisko' in a cursive font (similar to Velmo cycling brand) and 'Bike Brands' to be separate or below 'Brisko' in a simple capital letter font. The inclusion of an image reflective of the nature of the business would be encouraged.

Industry/Entity Type

Business

Contact Information for Business Card

2 cards with following information;

Dorian Pelt
Managing Director
E dorian@briskobikebrands-example.ae
M +971 (0) 56 482 3107
Trade Lic. No. TBA

Minna Pelt
Account Manager
E minna@briskobikebrands-example.ae
P +971 (0) 56 916 2583
Trade Lic. No. TBA

Requirements
Must have
• Full company name is 'Brisko Bike Brands'
• Would like Brisko to be separate and in a font similar to Velmo Cycling clothing, and would like Bike Brands to be in capitals below. Would consider if an image of a push bike between the text was presented.

```html
<!DOCTYPE html>
<html lang="en">
<head>
<meta charset="utf-8">
<title>Brisko Bike Brands – Business Card</title>
<link rel="stylesheet" href="https://fonts.googleapis.com/css2?family=Montserrat:wght@400;600;700&family=Quicksand:wght@300;400&display=swap">
<style>
  :root {
    --backdrop: #d9d6d1;
    --card: #24262b;
    --accent: #f5a500;
    --logo-grey: #c9ccd1;
    --tag-grey: #7d8086;
    --text-light: #c4c7cc;
    --rule: #8a8d93;
    --tab: #f4f4f4;
    --ink: #24262b;
  }
  * { box-sizing: border-box; margin: 0; padding: 0; }
  html, body {
    width: 1200px; height: 1200px; overflow: hidden;
    background: var(--backdrop);
  }
  .sheet { position: relative; width: 1200px; height: 1200px; }
  .card {
    position: absolute; left: 110px; width: 980px; height: 560px;
    background: var(--card);
    overflow: hidden;
    box-shadow: 0 10px 24px rgba(0,0,0,0.25);
  }
  .card--front { top: 30px; }
  .card--back  { top: 610px; }

  /* Front */
  .front-band {
    position: absolute; left: 0; right: 0; bottom: 0; height: 134px;
    background: var(--accent);
  }
  .brand {
    position: absolute; left: 400px; top: 118px;
    display: flex; align-items: flex-start; gap: 18px;
  }
  .brand-square {
    width: 118px; height: 118px; background: var(--accent); margin-top: 4px; flex: none;
  }
  .brand-text { display: flex; flex-direction: column; }
  .brand-name {
    font-family: "Quicksand", sans-serif; font-weight: 300;
    font-size: 96px; line-height: 1; color: var(--logo-grey);
    letter-spacing: 2px;
  }
  .brand-tag {
    font-family: "Montserrat", sans-serif; font-weight: 400;
    font-size: 15px; letter-spacing: 3px; color: var(--tag-grey);
    margin-top: 10px; padding-left: 6px;
  }

  /* Back */
  .brand--small { left: auto; right: 60px; top: 44px; gap: 8px; }
  .brand--small .brand-square { width: 44px; height: 44px; margin-top: 2px; }
  .brand--small .brand-name { font-size: 42px; letter-spacing: 1px; }
  .brand--small .brand-tag { font-size: 9px; letter-spacing: 2px; margin-top: 4px; padding-left: 3px; }

  .back-rule {
    position: absolute; left: 400px; right: 0; top: 160px;
    height: 3px; background: var(--rule);
  }
  .name-tab {
    position: absolute; left: 0; top: 160px; width: 410px; height: 108px;
    background: var(--tab);
    clip-path: polygon(0 0, 100% 0, 94% 100%, 0 100%);
    padding: 30px 0 0 60px;
  }
  .person-name {
    font-family: "Montserrat", sans-serif; font-weight: 400;
    font-size: 32px; color: var(--ink); letter-spacing: 1px; line-height: 1;
  }
  .person-name strong { font-weight: 600; }
  .person-title {
    font-family: "Montserrat", sans-serif; font-weight: 700;
    font-size: 17px; color: var(--ink); margin-top: 6px;
  }
  .contact-list {
    position: absolute; left: 130px; top: 318px;
    list-style: none;
  }
  .contact-item {
    display: flex; align-items: center; gap: 20px;
    height: 48px;
    font-family: "Montserrat", sans-serif; font-weight: 400;
    font-size: 19px; color: var(--text-light);
  }
  .contact-item svg { width: 24px; height: 24px; flex: none; }
</style>
</head>
<body>
<main class="sheet">

  <section class="card card--front" aria-label="Card front">
    <div class="brand">
      <span class="brand-square"></span>
      <div class="brand-text">
        <span class="brand-name">Brisko</span>
        <span class="brand-tag">BIKE BRANDS</span>
      </div>
    </div>
    <div class="front-band"></div>
  </section>

  <section class="card card--back" aria-label="Card back">
    <div class="brand brand--small">
      <span class="brand-square"></span>
      <div class="brand-text">
        <span class="brand-name">Brisko</span>
        <span class="brand-tag">BIKE BRANDS</span>
      </div>
    </div>
    <div class="back-rule"></div>
    <div class="name-tab">
      <p class="person-name">DORIAN <strong>PELT</strong></p>
      <p class="person-title">Managing Director</p>
    </div>
    <ul class="contact-list">
      <li class="contact-item">
        <svg viewBox="0 0 24 24" aria-hidden="true"><path fill="#c4c7cc" d="M12 2a7 7 0 0 0-7 7c0 5 7 13 7 13s7-8 7-13a7 7 0 0 0-7-7zm0 9.5A2.5 2.5 0 1 1 12 6.5a2.5 2.5 0 0 1 0 5z"/></svg>
        <span>PO Box 48210, Dubai, UAE</span>
      </li>
      <li class="contact-item">
        <svg viewBox="0 0 24 24" aria-hidden="true"><path fill="#c4c7cc" d="M6.6 10.8a15 15 0 0 0 6.6 6.6l2.2-2.2a1 1 0 0 1 1-.25 11 11 0 0 0 3.6.57 1 1 0 0 1 1 1V20a1 1 0 0 1-1 1A17 17 0 0 1 3 4a1 1 0 0 1 1-1h3.5a1 1 0 0 1 1 1c0 1.25.2 2.45.57 3.6a1 1 0 0 1-.25 1z"/></svg>
        <span>M +971 (0) 56 482 3107</span>
      </li>
      <li class="contact-item">
        <svg viewBox="0 0 24 24" aria-hidden="true"><path fill="#c4c7cc" d="M3 5h18v14H3zm2 2v.5l7 5 7-5V7l-7 5z"/></svg>
        <span>E dorian@briskobikebrands-example.ae</span>
      </li>
      <li class="contact-item">
        <svg viewBox="0 0 24 24" aria-hidden="true"><g fill="none" stroke="#c4c7cc" stroke-width="1.8"><rect x="5" y="3" width="14" height="18" rx="1"/><path d="M8 8h8M8 12h8M8 16h5"/></g></svg>
        <span>Trade Lic. No. TBA</span>
      </li>
    </ul>
  </section>

</main>
</body>
</html>
```